Website design needed for gift based dropship website

I am building a dropshipping website that will create gift based merchandise and send it out to our clients customers for them. Our clients will sell products and when a customer buys from them, we create the item and send it out to the customer.

I am looking for a very similar website to quillmarten.com - that website is doing a very similar thing to what i am doing but where the quillmarten website is based around clothing, my website will be based around gifts. Another website that i like that is doing a similar thing to what i will do is dravo.com

I require 2 pages to be made:
1) The home page
2) A landing page for a free product giveaway offer

1) THE HOME PAGE
The home page should be a merger of the two previously stated websites (www.dravo.com and www.quillmarten.com). The style fo the homepage should be based on the logo that is attached and the colour scheme should be similar but basic.

2) THE LANDING PAGE
The landing page will be giving away a free mobile phone cover. The page needs to have some mobile phone covers for different phones all with random designs on. The page should state that they can have any design that they want and they do not pay for the phone (they only pay for shipping).

Menu pages and text should be taken from the quillmarten.com website.

Target Market(s)

18 - 40 year old males. People who like the idea of earning extra money in their spare time but aren't too sure how to do it. Semi-professional jobs.

Number of Pages Required

2 page

Font styles to use
Serif
Sans Serif
Decorative
Script

Colors

Designer to choose colors to be used in the design.

Requirements
Must have
• A "how it works" image where the dropshipping process is explained to a visitor to the website (similar to the one on the quillmarten "how it works page")
Nice to have
• Testimonial area on homepage
Should not have
• Homepage should not have:
• - "latest orders from" area
• - Video
• - Warehousing/fulfilment area
• - Integration area
• -

```html
<!DOCTYPE html>
<html lang="en">
<head>
<meta charset="utf-8">
<title>Giftwell Prints – Personalised gifts and momentos</title>
<link rel="stylesheet" href="https://fonts.googleapis.com/css2?family=Roboto:wght@300;400&family=Roboto+Condensed:wght@700&family=Caveat:wght@400&display=swap">
<style>
  :root {
    --plum: #3d0c22;
    --plum-soft: #5a3a45;
    --red: #ee1100;
    --hero-bg: #e6e2e3;
    --text: #222;
    --text-muted: #4a4a4a;
    --text-faint: #9a7f86;
    --line: #d6d6d6;
    --white: #fff;
  }
  * { box-sizing: border-box; margin: 0; padding: 0; }
  html, body { width: 1200px; height: 1200px; overflow: hidden; }
  body { position: relative; font-family: "Roboto", Helvetica, Arial, sans-serif; background: var(--white); color: var(--text); }

  .account-bar { position: absolute; top: 0; left: 0; width: 1200px; height: 38px; background: var(--white); }
  .account-link { position: absolute; top: 9px; font-size: 16px; color: #555; display: flex; align-items: center; gap: 4px; }
  .account-link svg { width: 10px; height: 10px; fill: #777; }
  .account-link.login { left: 872px; }
  .account-link.signup { left: 968px; }

  .site-header { position: absolute; top: 38px; left: 0; width: 1200px; height: 172px; background: linear-gradient(#f3f3f3, #fff 40%); }
  .brand { position: absolute; left: 152px; top: 62px; display: flex; align-items: center; gap: 12px; }
  .brand-mark { width: 56px; height: 56px; border-radius: 50%; background: var(--plum); }
  .brand-name { font-family: "Roboto Condensed", sans-serif; font-weight: 700; font-size: 40px; line-height: 40px; color: var(--plum); text-transform: uppercase; }

  .main-nav { position: absolute; left: 422px; top: 18px; width: 618px; height: 39px; border-bottom: 1px solid var(--line); }
  .main-nav a { position: absolute; top: 0; font-size: 16px; color: var(--text); text-decoration: none; }

  .social { position: absolute; left: 778px; top: 98px; display: flex; align-items: center; }
  .social-label { font-family: "Caveat", cursive; font-size: 26px; color: var(--red); }
  .social-label svg { width: 22px; height: 12px; vertical-align: middle; margin-left: 6px; }
  .social-dot { position: absolute; top: 6px; width: 18px; height: 18px; border-radius: 4px; background: var(--red); }

  .hero { position: absolute; top: 210px; left: 0; width: 1200px; height: 611px; background: var(--hero-bg); }
  .hero-title { position: absolute; left: 148px; top: 110px; font-family: "Roboto Condensed", sans-serif; font-weight: 700; font-size: 78px; line-height: 80px; color: var(--plum); letter-spacing: -0.5px; }
  .hero-lead { position: absolute; left: 148px; top: 296px; font-size: 32px; line-height: 38px; font-weight: 300; color: var(--text-muted); }
  .btn { position: absolute; display: flex; align-items: center; justify-content: center; background: var(--red); color: var(--white); font-family: "Roboto Condensed", sans-serif; font-weight: 700; text-decoration: none; }
  .hero .btn { left: 150px; top: 412px; width: 249px; height: 56px; font-size: 24px; }
  .phone-case { position: absolute; left: 781px; top: 39px; width: 260px; height: 533px; border-radius: 38px; background: radial-gradient(circle at 50% 50%, #fff 0%, #f4e9ea 55%, #e9d7da 100%); border: 1px solid #ccc; box-shadow: 0 4px 6px rgba(0,0,0,.2); }

  .paths { position: absolute; top: 821px; left: 0; width: 1200px; height: 379px; background: linear-gradient(#fff, #f1f1f1); }
  .paths-divider { position: absolute; left: 594px; top: 0; width: 1px; height: 379px; background: var(--line); }
  .paths-or { position: absolute; left: 565px; top: 218px; width: 58px; height: 58px; border-radius: 50%; background: var(--white); border: 1px solid var(--line); display: flex; align-items: center; justify-content: center; font-size: 24px; color: var(--plum-soft); }
  .path { position: absolute; top: 0; width: 440px; text-align: center; }
  .path.personal { left: 151px; }
  .path.seller { left: 598px; }
  .path-icon { position: absolute; top: 41px; }
  .path.personal .path-icon { left: 185px; width: 64px; height: 88px; background: linear-gradient(#e9e4e6 55%, var(--red) 55%); border-radius: 32px 32px 0 0; }
  .path.seller .path-icon { left: 166px; width: 116px; height: 76px; top: 53px; background: linear-gradient(#8a6a74 30%, var(--red) 30%); }
  .path-title { position: absolute; left: 0; width: 440px; top: 148px; font-family: "Roboto Condensed", sans-serif; font-weight: 700; font-size: 37px; color: var(--plum-soft); }
  .path-text { position: absolute; left: 0; width: 440px; top: 218px; font-size: 16px; line-height: 24px; color: var(--text-faint); }
  .path .btn { top: 290px; left: 112px; width: 216px; height: 48px; font-size: 21px; }
</style>
</head>
<body>
  <div class="account-bar">
    <span class="account-link login"><svg viewBox="0 0 10 10"><circle cx="5" cy="3" r="2.5"/><path d="M0 10c0-3 2-4.5 5-4.5s5 1.5 5 4.5z"/></svg>Login</span>
    <span class="account-link signup"><svg viewBox="0 0 10 10"><circle cx="5" cy="3" r="2.5"/><path d="M0 10c0-3 2-4.5 5-4.5s5 1.5 5 4.5z"/></svg>Sign up</span>
  </div>

  <header class="site-header">
    <div class="brand">
      <span class="brand-mark"></span>
      <span class="brand-name">Giftwell<br>Prints</span>
    </div>
    <nav class="main-nav">
      <a style="left:9px">Products</a>
      <a style="left:108px">How it works</a>
      <a style="left:236px">Mockup Generator</a>
      <a style="left:412px">Shipping</a>
      <a style="left:515px">FAQ</a>
      <a style="left:587px">Blog</a>
    </nav>
    <div class="social">
      <span class="social-label">Social Media:<svg viewBox="0 0 22 12"><path d="M1 8 Q10 5 20 4 M14 1 L20 4 L15 9" fill="none" stroke="#ee1100" stroke-width="1.6"/></svg></span>
    </div>
    <span class="social-dot" style="left:935px;top:104px" aria-label="Social link"></span>
    <span class="social-dot" style="left:977px;top:104px" aria-label="Social link"></span>
    <span class="social-dot" style="left:1021px;top:104px" aria-label="Social link"></span>
  </header>

  <section class="hero">
    <h1 class="hero-title">Personalised gifts<br>and momentos</h1>
    <p class="hero-lead">Add your personalised message<br>or image to any of our products</p>
    <a class="btn">View Product Range</a>
    <div class="phone-case" role="img" aria-label="White phone case printed with a repeating heart and gift pattern"></div>
  </section>

  <section class="paths">
    <div class="paths-divider"></div>
    <div class="path personal">
      <div class="path-icon" role="img" aria-label="Illustration of a customer"></div>
      <h2 class="path-title">Print designs for yourself</h2>
      <p class="path-text">One-off designs that you want to have<br>printed for your own use</p>
      <a class="btn">Get Started</a>
    </div>
    <div class="paths-or">or</div>
    <div class="path seller">
      <div class="path-icon" role="img" aria-label="Illustration of a shop front"></div>
      <h2 class="path-title">Sell designs online</h2>
      <p class="path-text">If you want to sell your designs in an online<br>store or marketplace</p>
      <a class="btn">Connect Your Shop</a>
    </div>
  </section>
</body>
</html>
```